Pelican Drift - Caffeine Supplement for everyday use & pre-workout

Online marketplace focussing on caffeine supplements for everyday use and pre-workouts. Selling point is this product is not as strong as the existing pre-workouts to avoid crashing and uncomfortable levels of energy. Ideal for endurance sports athletes as an inter-workout supplement to maintain energy levels. Initially 4 categories, stand-alone tubs, stacks (2/3 tubs), taster packs and merchandise (shaker bottles) etc.

Target Market(s)

under 40s across the fitness imdustry

Industry/Entity Type

Supplement

Coding

Coded - Design and coding required

Font styles to use
Sans Serif

Colors
ec1f27
ffffff

Requirements
Must have
• Home Page
About Page
Product Page
Contact Page
Basket
Woocommerce capability
Nice to have
• Fixed Header so when scrolling it remains fixed on page.

Logo on left hand side. 4 links on the right hand side (Home, Products, About, Basket)

```html
<!DOCTYPE html>
<html lang="en">
<head>
<meta charset="utf-8">
<title>Pelican Drift – Caffeine Supplements</title>
<link rel="stylesheet" href="https://fonts.googleapis.com/css2?family=Montserrat:wght@400;600;700;800&family=Open+Sans:wght@400;600;700&display=swap">
<style>
:root{
  --red:#ec1f27;
  --white:#ffffff;
  --ink:#1b1b1b;
  --text:#555555;
  --muted:#8a8a8a;
  --light:#f5f5f5;
  --dark:#141414;
  --star:#f5b400;
}
*{box-sizing:border-box;margin:0;padding:0}
html,body{width:1200px;height:4843px;overflow:hidden}
body{font-family:"Open Sans",sans-serif;color:var(--ink);background:var(--white);position:relative}
a{color:inherit;text-decoration:none}
.wrap{width:1000px;margin:0 auto;position:relative}

/* top bar */
.topbar{height:41px;background:var(--red);color:var(--white);font-family:"Montserrat",sans-serif;font-size:11px;font-weight:600}
.topbar .wrap{display:flex;align-items:center;height:41px}
.topbar .ship{display:flex;align-items:center;gap:8px;white-space:nowrap}
.topbar .right{margin-left:auto;display:flex;align-items:center;gap:18px;white-space:nowrap}
.topbar .item{display:flex;align-items:center;gap:7px}
.social{display:flex;gap:10px}
.social span{width:16px;height:16px;border-radius:50%;border:1.5px solid rgba(255,255,255,.85);display:block}
.lang{background:var(--white);color:var(--ink);border-radius:12px;padding:3px 12px;font-size:11px;display:flex;gap:5px;align-items:center}

/* nav */
.nav{height:68px;border-bottom:1px solid #eee}
.nav .wrap{height:68px}
.brand{position:absolute;left:0;top:0;height:68px;display:flex;align-items:center;gap:8px;font-family:"Montserrat",sans-serif;font-weight:800;font-size:22px;color:var(--ink);white-space:nowrap}
.brand .dot{width:14px;height:14px;border-radius:50%;background:var(--red)}
.menu{position:absolute;left:278px;top:0;height:68px;display:flex;align-items:center;gap:38px;font-family:"Montserrat",sans-serif;font-size:13px;font-weight:600;white-space:nowrap}
.search{position:absolute;left:760px;top:17px;width:188px;height:34px;background:#ececec;border-radius:17px}
.search svg{position:absolute;right:12px;top:9px}
.cart{position:absolute;left:976px;top:25px}
.cart b{position:absolute;top:-6px;right:-7px;background:var(--red);color:#fff;font-size:8px;width:12px;height:12px;border-radius:50%;text-align:center;line-height:12px}

/* hero */
.hero{height:583px;position:relative;background:linear-gradient(100deg,#2c2c2e 0%,#4a4a4c 35%,#6d7078 60%,#8d8a86 100%)}
.hero .photo{position:absolute;inset:0}
.hero .tubs{position:absolute;left:370px;top:295px;width:540px;height:285px;background:linear-gradient(180deg,#55504f,#1e1e1e);border-radius:24px 24px 12px 12px;opacity:.85}
.hero .copy{position:absolute;left:100px;top:153px;color:var(--white)}
.hero .kicker{font-family:"Montserrat",sans-serif;font-size:22px;font-weight:400;letter-spacing:.5px}
.hero h1{font-family:"Montserrat",sans-serif;font-size:43px;font-weight:800;line-height:46px;margin-top:18px;letter-spacing:.5px}
.hero p{font-size:16px;margin-top:8px}
.btn{display:inline-flex;align-items:center;gap:6px;background:var(--red);color:var(--white);font-family:"Montserrat",sans-serif;font-weight:700;font-size:13px;border-radius:22px;padding:0 20px;height:42px}
.hero .btn{margin-top:20px}

/* section heads */
.head{text-align:center}
.head h2{font-family:"Montserrat",sans-serif;font-size:29px;font-weight:700;letter-spacing:.5px;color:var(--ink)}
.head p{font-size:14px;color:var(--text);margin-top:20px}

/* categories */
.cats{height:497px;padding-top:83px}
.cat-grid{display:grid;grid-template-columns:repeat(4,241px);gap:12px;margin-top:40px}
.cat{height:235px;position:relative;overflow:hidden}
.cat .fill{position:absolute;inset:0}
.cat .label{position:absolute;left:0;right:0;bottom:0;height:42px;background:rgba(25,25,25,.85);color:#fff;display:flex;align-items:center;padding:0 12px;font-family:"Montserrat",sans-serif;font-weight:600;font-size:15px;white-space:nowrap}
.cat .label i{margin-left:auto;width:22px;height:22px;border:1.5px solid #fff;border-radius:50%;display:flex;align-items:center;justify-content:center}

/* featured */
.featured{height:1149px;background:var(--light);padding-top:77px}
.prod-grid{display:grid;grid-template-columns:repeat(3,316px);column-gap:26px;row-gap:27px;margin-top:40px}
.card{height:397px;background:var(--white);position:relative;text-align:center;box-shadow:0 1px 4px rgba(0,0,0,.05)}
.card .heart{position:absolute;right:14px;top:14px}
.card .pack{width:118px;height:158px;margin:25px auto 0;border-radius:10px;background:linear-gradient(180deg,#3a3a3a,#111)}
.card .pack.bottle{width:70px;border-radius:16px}
.card h3{font-family:"Montserrat",sans-serif;font-size:19px;font-weight:700;margin-top:20px;letter-spacing:.3px}
.card .price{color:var(--red);font-size:24px;margin-top:6px}
.stars{color:var(--star);font-size:13px;letter-spacing:1px;margin-top:4px}
.card .rev{color:var(--red);font-size:13px;text-decoration:underline;margin-top:3px}
.card .actions{display:flex;justify-content:center;gap:10px;margin-top:22px}
.flav{height:34px;border:1px solid #333;border-radius:17px;padding:0 10px;display:flex;align-items:center;gap:4px;font-family:"Montserrat",sans-serif;font-size:11px;font-weight:700;white-space:nowrap}
.add{height:34px;background:var(--red);color:#fff;border-radius:17px;padding:0 14px;display:flex;align-items:center;gap:6px;font-family:"Montserrat",sans-serif;font-size:11px;font-weight:700;white-space:nowrap}
.view{display:block;text-align:center;color:var(--red);font-family:"Montserrat",sans-serif;font-weight:700;font-size:13px;text-decoration:underline;margin-top:40px}

/* banners */
.banner{height:423px;position:relative;overflow:hidden;color:#fff}
.banner .bg{position:absolute;inset:0}
.banner .inner{position:absolute;left:0;right:0;top:75px;text-align:center}
.mini-brand{display:inline-flex;align-items:center;gap:6px;font-family:"Montserrat",sans-serif;font-weight:800;font-size:18px}
.mini-brand .dot{width:10px;height:10px;border-radius:50%;background:var(--red)}
.banner .kick{font-family:"Montserrat",sans-serif;font-size:24px;font-weight:400;letter-spacing:1px;margin-top:16px}
.banner h2{font-family:"Montserrat",sans-serif;font-size:46px;font-weight:800;letter-spacing:1.5px;margin-top:6px;line-height:56px}
.banner p{font-size:17px;line-height:27px;margin-top:8px}
.banner .btn{margin-top:20px}

/* reviews */
.reviews{height:559px;padding-top:88px}
.rev-grid{display:grid;grid-template-columns:repeat(3,316px);gap:26px;margin-top:46px}
.review{height:244px;background:var(--light);padding:22px 20px}
.quote{width:44px;height:44px;border-radius:50%;background:var(--red);display:flex;align-items:center;justify-content:center}
.review p{font-size:12.5px;line-height:20px;color:var(--text);margin-top:14px}
.review .stars{margin-top:2px}
.review .name{font-family:"Montserrat",sans-serif;font-size:13px;font-weight:700;margin-top:4px}

/* social feed */
.feed{height:724px;padding-top:87px}
.feed-grid{display:grid;grid-template-columns:repeat(4,241px);gap:15px 12px;margin-top:40px}
.shot{height:233px;position:relative}
.shot .ring{position:absolute;left:50%;top:50%;width:44px;height:44px;margin:-22px 0 0 -22px;border:3px solid #fff;border-radius:50%}

/* footer */
.footer{height:376px;background:var(--dark);color:#fff;position:relative}
.footer .cols{position:absolute;top:81px;left:100px;right:100px}
.f-brand{position:absolute;left:0;top:8px;display:flex;align-items:center;gap:10px;font-family:"Montserrat",sans-serif;font-weight:800;font-size:28px;white-space:nowrap}
.f-brand .dot{width:16px;height:16px;border-radius:50%;background:var(--red)}
.f-about{position:absolute;left:0;top:95px;width:230px;font-size:11.5px;line-height:21px;color:#d8d8d8}
.f-col{position:absolute;top:0}
.f-col h4{font-family:"Montserrat",sans-serif;font-size:16px;font-weight:700;letter-spacing:.3px;white-space:nowrap}
.f-col ul{list-style:none;margin-top:8px}
.f-col li{font-size:14px;line-height:25.5px;color:#e6e6e6;white-space:nowrap}
.contact li{display:flex;gap:14px;font-size:14px;line-height:22px;margin-bottom:20px}
.contact svg{flex:none;margin-top:4px}
.f-bottom{position:absolute;left:100px;right:100px;bottom:28px;display:flex;align-items:center;font-size:12px;color:#d8d8d8}
.f-bottom .social{margin-left:auto;gap:14px}
.f-bottom .social span{width:15px;height:15px;border-color:#fff}
</style>
</head>
<body>

<header>
  <div class="topbar">
    <div class="wrap">
      <div class="ship">
        <svg width="18" height="12" viewBox="0 0 18 12"><rect x="0" y="1" width="11" height="8" fill="#fff"/><path d="M11 4h4l3 3v2h-7z" fill="#fff"/><circle cx="4" cy="10" r="2" fill="#fff"/><circle cx="14" cy="10" r="2" fill="#fff"/></svg>
        FLAT RATE SHIPPING ON ALL ORDERS
      </div>
      <div class="right">
        <div class="item"><svg width="12" height="12" viewBox="0 0 24 24"><path d="M6.6 10.8a15 15 0 0 0 6.6 6.6l2.2-2.2a1 1 0 0 1 1-.25 11.4 11.4 0 0 0 3.6.57 1 1 0 0 1 1 1V20a1 1 0 0 1-1 1A17 17 0 0 1 3 4a1 1 0 0 1 1-1h3.5a1 1 0 0 1 1 1c0 1.25.2 2.45.57 3.57a1 1 0 0 1-.25 1z" fill="#fff"/></svg>555 014 2290</div>
        <div class="item"><svg width="13" height="13" viewBox="0 0 24 24"><circle cx="12" cy="7" r="5" fill="#fff"/><path d="M2 23c0-6 4.5-9 10-9s10 3 10 9z" fill="#fff"/></svg>MY ACCOUNT</div>
        <div class="social" aria-label="Social links"><span></span><span></span><span></span><span></span></div>
        <div class="lang">EN <svg width="8" height="5" viewBox="0 0 8 5"><path d="M1 1l3 3 3-3" stroke="#333" fill="none" stroke-width="1.3"/></svg></div>
      </div>
    </div>
  </div>
  <nav class="nav">
    <div class="wrap">
      <a class="brand" href="#"><span class="dot"></span>Pelican Drift</a>
      <div class="menu"><a href="#">HOME</a><a href="#">PRODUCTS</a><a href="#">ABOUT</a><a href="#">BASKET</a><a href="#">CONTACT</a></div>
      <div class="search"><svg width="16" height="16" viewBox="0 0 16 16"><circle cx="9" cy="7" r="5" stroke="#333" stroke-width="1.5" fill="none"/><path d="M5.5 10.5L1.5 14.5" stroke="#333" stroke-width="1.5"/></svg></div>
      <div class="cart"><svg width="20" height="18" viewBox="0 0 24 22"><path d="M1 2h4l3 11h12l3-8H7" stroke="var(--red)" stroke-width="2.4" fill="none"/><circle cx="9" cy="18" r="2" fill="var(--red)"/><circle cx="18" cy="18" r="2" fill="var(--red)"/></svg><b>0</b></div>
    </div>
  </nav>
</header>

<section class="hero">
  <div class="photo" role="img" aria-label="Woman drinking from a shaker bottle in a gym"></div>
  <div class="tubs" role="img" aria-label="Three supplement tubs with berries and strawberries"></div>
  <div class="copy">
    <div class="kicker">MAINTAINS BONE STRENGHT!</div>
    <h1>CAFFEINE<br>SUPPLEMENTS</h1>
    <p>for everyday use and pre-workouts</p>
    <a class="btn" href="#">BUY NOW <svg width="12" height="8" viewBox="0 0 12 8"><path d="M0 4h10M7 1l3 3-3 3" stroke="#fff" fill="none" stroke-width="1.3"/></svg></a>
  </div>
</section>

<section class="cats">
  <div class="wrap">
    <div class="head"><h2>SHOP BY CATEGORIES</h2><p>Lorem ipsum dolor sit amet, consectetur adipiscing elit, sed</p></div>
    <div class="cat-grid">
      <div class="cat"><div class="fill" role="img" aria-label="Woman holding a supplement tub in a gym" style="background:linear-gradient(160deg,#bfc3c8,#6c7076)"></div><div class="label">STAND-ALONE TUBS<i><svg width="8" height="10" viewBox="0 0 8 10"><path d="M2 1l4 4-4 4" stroke="#fff" fill="none" stroke-width="1.4"/></svg></i></div></div>
      <div class="cat"><div class="fill" role="img" aria-label="Scoop of protein powder" style="background:linear-gradient(160deg,#d9c3a8,#8e6a48)"></div><div class="label">STACKS (2/3 TUBS)<i><svg width="8" height="10" viewBox="0 0 8 10"><path d="M2 1l4 4-4 4" stroke="#fff" fill="none" stroke-width="1.4"/></svg></i></div></div>
      <div class="cat"><div class="fill" role="img" aria-label="Man with supplement tub by a brick wall" style="background:linear-gradient(160deg,#a0735a,#3d3634)"></div><div class="label">TASTER PACKS<i><svg width="8" height="10" viewBox="0 0 8 10"><path d="M2 1l4 4-4 4" stroke="#fff" fill="none" stroke-width="1.4"/></svg></i></div></div>
      <div class="cat"><div class="fill" role="img" aria-label="Woman drinking from a shaker bottle" style="background:linear-gradient(160deg,#8c6e5e,#2f2a29)"></div><div class="label">MERCHANDISE<i><svg width="8" height="10" viewBox="0 0 8 10"><path d="M2 1l4 4-4 4" stroke="#fff" fill="none" stroke-width="1.4"/></svg></i></div></div>
    </div>
  </div>
</section>

<section class="featured">
  <div class="wrap">
    <div class="head"><h2>FEATURED PRODUCTS</h2><p>Lorem ipsum dolor sit amet, consectetur adipiscing elit, sed</p></div>
    <div class="prod-grid">
      <div class="card"><svg class="heart" width="22" height="20" viewBox="0 0 24 22"><path d="M12 21L2 11a5.5 5.5 0 0 1 10-7 5.5 5.5 0 0 1 10 7z" fill="#ddd"/></svg><div class="pack" role="img" aria-label="Mass gainer pouch"></div><h3>PRODUCT NAME</h3><div class="price">$35.00</div><div class="stars">★★★★★</div><div class="rev">123 REVIEWS</div><div class="actions"><span class="flav">ADD FLAVOUR ⌄</span><span class="add">ADD TO CART</span></div></div>
      <div class="card"><svg class="heart" width="22" height="20" viewBox="0 0 24 22"><path d="M12 21L2 11a5.5 5.5 0 0 1 10-7 5.5 5.5 0 0 1 10 7z" fill="#ddd"/></svg><div class="pack" role="img" aria-label="Amino acid tub" style="width:86px"></div><h3>PRODUCT NAME</h3><div class="price">$35.00</div><div class="stars">★★★★★</div><div class="rev">123 REVIEWS</div><div class="actions"><span class="flav">ADD FLAVOUR ⌄</span><span class="add">ADD TO CART</span></div></div>
      <div class="card"><svg class="heart" width="22" height="20" viewBox="0 0 24 22"><path d="M12 21L2 11a5.5 5.5 0 0 1 10-7 5.5 5.5 0 0 1 10 7z" fill="#ddd"/></svg><div class="pack" role="img" aria-label="Creatine tub"></div><h3>PRODUCT NAME</h3><div class="price">$35.00</div><div class="stars">★★★★★</div><div class="rev">123 REVIEWS</div><div class="actions"><span class="flav">ADD FLAVOUR ⌄</span><span class="add">ADD TO CART</span></div></div>
      <div class="card"><svg class="heart" width="22" height="20" viewBox="0 0 24 22"><path d="M12 21L2 11a5.5 5.5 0 0 1 10-7 5.5 5.5 0 0 1 10 7z" fill="#ddd"/></svg><div class="pack" role="img" aria-label="Amino acid tub" style="width:86px"></div><h3>PRODUCT NAME</h3><div class="price">$35.00</div><div class="stars">★★★★★</div><div class="rev">123 REVIEWS</div><div class="actions"><span class="flav">ADD FLAVOUR ⌄</span><span class="add">ADD TO CART</span></div></div>
      <div class="card"><svg class="heart" width="22" height="20" viewBox="0 0 24 22"><path d="M12 21L2 11a5.5 5.5 0 0 1 10-7 5.5 5.5 0 0 1 10 7z" fill="#ddd"/></svg><div class="pack" role="img" aria-label="Protein tub" style="width:98px"></div><h3>PRODUCT NAME</h3><div class="price">$35.00</div><div class="stars">★★★★★</div><div class="rev">123 REVIEWS</div><div class="actions"><span class="flav">ADD FLAVOUR ⌄</span><span class="add">ADD TO CART</span></div></div>
      <div class="card"><svg class="heart" width="22" height="20" viewBox="0 0 24 22"><path d="M12 21L2 11a5.5 5.5 0 0 1 10-7 5.5 5.5 0 0 1 10 7z" fill="#ddd"/></svg><div class="pack bottle" role="img" aria-label="Shaker bottle"></div><h3>PRODUCT NAME</h3><div class="price">$35.00</div><div class="stars">★★★★★</div><div class="rev">123 REVIEWS</div><div class="actions"><span class="flav">ADD FLAVOUR ⌄</span><span class="add">ADD TO CART</span></div></div>
    </div>
    <a class="view" href="#">VIEW ALL PRODUCTS</a>
  </div>
</section>

<section class="banner">
  <div class="bg" role="img" aria-label="Athlete lifting a dumbbell beside a protein tub on a dark background" style="background:linear-gradient(90deg,#3a3a3a 0%,#1e1e1e 30%,#141414 55%,#262626 80%,#1a1a1a 100%)"></div>
  <div class="inner">
    <div class="mini-brand"><span class="dot"></span>Pelican Drift</div>
    <div class="kick">NATURAL INGREDIENTS</div>
    <h2>QUALITY &amp; SAFETY</h2>
    <p>Our goal is to provide both a superior customer experience<br>and tremendous value for our customers.</p>
    <a class="btn" href="#">BUY NOW <svg width="12" height="8" viewBox="0 0 12 8"><path d="M0 4h10M7 1l3 3-3 3" stroke="#fff" fill="none" stroke-width="1.3"/></svg></a>
  </div>
</section>

<section class="reviews">
  <div class="wrap">
    <div class="head"><h2>LATEST REVIEWS</h2><p>Lorem ipsum dolor sit amet, consectetur adipiscing elit, sed</p></div>
    <div class="rev-grid">
      <div class="review"><div class="quote"><svg width="20" height="16" viewBox="0 0 20 16"><path d="M0 16V9C0 4 2 1 7 0l1 2C5 3 4 5 4 7h4v9zm11 0V9c0-5 2-8 7-9l1 2c-3 1-4 3-4 5h4v9z" fill="#fff"/></svg></div><p>Lorem ipsum dolor sit amet, tetur adng elit, sd do eiusmod teor incididunt ut labore et dolore magna aliqua.is ipsum suspe ultrices gravida. Risus commodo viverra maecenas accumsan lacus vel facilisis.</p><div class="stars">★★★★★</div><div class="name">JOHN DOE</div></div>
      <div class="review"><div class="quote"><svg width="20" height="16" viewBox="0 0 20 16"><path d="M0 16V9C0 4 2 1 7 0l1 2C5 3 4 5 4 7h4v9zm11 0V9c0-5 2-8 7-9l1 2c-3 1-4 3-4 5h4v9z" fill="#fff"/></svg></div><p>Lorem ipsum dolor sit amet, tetur adng elit, sd do eiusmod teor incididunt ut labore et dolore magna aliqua.is ipsum suspe ultrices gravida. Risus commodo viverra maecenas accumsan lacus vel facilisis.</p><div class="stars">★★★★★</div><div class="name">JOHN DOE</div></div>
      <div class="review"><div class="quote"><svg width="20" height="16" viewBox="0 0 20 16"><path d="M0 16V9C0 4 2 1 7 0l1 2C5 3 4 5 4 7h4v9zm11 0V9c0-5 2-8 7-9l1 2c-3 1-4 3-4 5h4v9z" fill="#fff"/></svg></div><p>Lorem ipsum dolor sit amet, tetur adng elit, sd do eiusmod teor incididunt ut labore et dolore magna aliqua.is ipsum suspe ultrices gravida. Risus commodo viverra maecenas accumsan lacus vel facilisis.</p><div class="stars">★★★★★</div><div class="name">JOHN DOE</div></div>
    </div>
    <a class="view" href="#" style="margin-top:28px">VIEW ALL REVIEWS</a>
  </div>
</section>

<section class="banner">
  <div class="bg" role="img" aria-label="Mass gainer pouch and a woman training with a kettlebell" style="background:linear-gradient(90deg,#2b3138 0%,#3c434b 35%,#444a52 60%,#5a5350 85%,#3b3836 100%)"></div>
  <div class="inner">
    <div class="mini-brand"><span class="dot"></span>Pelican Drift</div>
    <div class="kick">PROVEN INGREDIENTS</div>
    <h2>JOIN THE TEAM</h2>
    <p>Our goal is to provide both a superior customer experience<br>and tremendous value for our customers.</p>
    <a class="btn" href="#">BUY NOW <svg width="12" height="8" viewBox="0 0 12 8"><path d="M0 4h10M7 1l3 3-3 3" stroke="#fff" fill="none" stroke-width="1.3"/></svg></a>
  </div>
</section>

<section class="feed">
  <div class="wrap">
    <div class="head"><h2>FOLLOW US ON SOCIAL</h2><p>Lorem ipsum dolor sit amet, consectetur adipiscing elit, sed</p></div>
    <div class="feed-grid">
      <div class="shot" role="img" aria-label="Woman stretching in a gym" style="background:linear-gradient(160deg,#c9a78a,#5e4a40)"></div>
      <div class="shot" role="img" aria-label="Athlete with rope from behind" style="background:linear-gradient(160deg,#7a7d80,#2d2e30)"></div>
      <div class="shot" role="img" aria-label="Woman doing a lunge, red overlay" style="background:linear-gradient(160deg,#e8706f,#c9474b)"><span class="ring"></span></div>
      <div class="shot" role="img" aria-label="Muscular man in dark studio light" style="background:linear-gradient(160deg,#8a6a55,#1f1a18)"></div>
      <div class="shot" role="img" aria-label="Runner's legs on a track" style="background:linear-gradient(160deg,#6e8398,#b0523a)"></div>
      <div class="shot" role="img" aria-label="Man posing in a gym" style="background:linear-gradient(160deg,#a4a7a9,#3f4244)"></div>
      <div class="shot" role="img" aria-label="Sneakers beside a barbell" style="background:linear-gradient(160deg,#55606a,#1e2327)"></div>
      <div class="shot" role="img" aria-label="Woman doing crunches on a mat" style="background:linear-gradient(160deg,#9a9593,#3a3634)"></div>
    </div>
  </div>
</section>

<footer class="footer">
  <div class="cols">
    <div class="f-brand"><span class="dot"></span>Pelican Drift</div>
    <p class="f-about">Lorem ipsum dolor sit ametconsectetur adipiscing elit, sed do eiusmod tempor incididunt ut labore et dolore magna aliqua.</p>
    <div class="f-col" style="left:310px"><h4>QUICK LINKS</h4><ul><li>Home</li><li>Our Firm</li><li>Info Center</li><li>Blog</li><li>News</li><li>Press</li></ul></div>
    <div class="f-col" style="left:519px"><h4>USEFUL LINKS</h4><ul><li>Profile</li><li>Offers</li><li>Cash Back</li><li>Cancel Order</li><li>Cart</li><li>Help</li></ul></div>
    <div class="f-col contact" style="left:743px"><h4>CONTACT INFO</h4>
      <ul style="margin-top:14px">
        <li><svg width="12" height="14" viewBox="0 0 12 16"><path d="M6 0a6 6 0 0 1 6 6c0 4-6 10-6 10S0 10 0 6a6 6 0 0 1 6-6z" fill="var(--red)"/><circle cx="6" cy="6" r="2" fill="#141414"/></svg><span>48 Harbour Lane Brightwater<br>30417</span></li>
        <li><svg width="13" height="13" viewBox="0 0 24 24"><path d="M6.6 10.8a15 15 0 0 0 6.6 6.6l2.2-2.2a1 1 0 0 1 1-.25 11.4 11.4 0 0 0 3.6.57 1 1 0 0 1 1 1V20a1 1 0 0 1-1 1A17 17 0 0 1 3 4a1 1 0 0 1 1-1h3.5a1 1 0 0 1 1 1c0 1.25.2 2.45.57 3.57a1 1 0 0 1-.25 1z" fill="var(--red)"/></svg><span>(555) 014 2290</span></li>
        <li><svg width="14" height="11" viewBox="0 0 14 10"><rect width="14" height="10" fill="var(--red)"/><path d="M0 0l7 5 7-5" stroke="#141414" fill="none"/></svg><span>hello@pelicandrift.example</span></li>
      </ul>
    </div>
  </div>
  <div class="f-bottom">
    <span>© 2020 Pelican-Drift. All Rights Reserved.</span>
    <div class="social" aria-label="Social links"><span></span><span></span><span></span><span></span></div>
  </div>
</footer>

</body>
</html>
```